Progressive and innovative Russian bank needs Landing Page for debit card with APR profit 9%

We need a web-design of the Landing Page for our new online retail financial service for Russian customers, debit card, named 'Harvest Card'. Harvest Card - is the debit stand-alone card (debit card not linked to a term deposit). Clients is getting profit (% on it's cash balance) depending on amount of cash:
- up to 30000₽ - 0%, 30000.01-700000₽ - 9% APR, more 700000₽ - 5% APR
- up to 1000$/€ - 0%, 1000-15000$/€ - 4% APR, more 15000$/€ - 2% APR
Clients can use the card as usual debit card for purchases in shops and payments (via internet too), etc. Traffic to the Landing Page come from ads in Searlo and Vokrum (Russian Searlo). We would like to see designs that use our brand colors and logo. The final design should follow brand limitations. Files in psd format.
Северный Вековой Банк

Reason: Thank you all. Our task was to make design of Landing page of the product. Majority of designs was the design of corporate site webpage. Please refine on your design.

```html
<!DOCTYPE html>
<html lang="en">
<head>
<meta charset="utf-8">
<title>Harvest Card — Card Features</title>
<link href="https://fonts.googleapis.com/css2?family=Arimo:wght@400;700&family=Inter:wght@300;400&display=swap" rel="stylesheet">
<style>
  :root {
    --ink: #1e1e1e;
    --body: #3a3a3a;
    --brand-blue: #2a6aa6;
    --apply-blue: #0b559e;
    --lime: #c3cf1c;
    --ring: #c8d200;
    --card-bg: #eeefee;
    --rule: #dcdcdc;
    --white: #ffffff;
  }
  * { box-sizing: border-box; margin: 0; padding: 0; }
  html, body { width: 1200px; height: 865px; overflow: hidden; background: var(--white); }
  body { position: relative; font-family: "Arimo", Arial, sans-serif; color: var(--ink); }

  .top-rule { position: absolute; left: 244px; top: 23px; width: 712px; border-top: 1px solid var(--rule); }

  .section-title {
    position: absolute; top: 62px; left: 0; width: 1200px; text-align: center;
    font-family: "Inter", Arial, sans-serif; font-weight: 300; font-size: 23px; color: var(--ink);
  }

  .feature { position: absolute; top: 130px; width: 231px; }
  .feature--benefits { left: 244px; }
  .feature--security { left: 485px; }
  .feature--access { left: 725px; }

  .feature-icon {
    display: block; width: 70px; height: 70px; margin: 0 auto;
  }
  .feature-name {
    margin-top: 10px; text-align: center; font-weight: 700; font-size: 15px; color: var(--brand-blue);
  }
  .feature--access .feature-name { margin-top: 15px; }

  .feature-card {
    position: absolute; top: 266px; width: 231px; height: 472px;
    background: var(--card-bg); border-radius: 5px 5px 0 0;
    padding: 10px 14px 0; text-align: center;
  }
  .feature-card--benefits { left: 244px; }
  .feature-card--security { left: 485px; }
  .feature-card--access { left: 725px; }

  .perk { margin-bottom: 28px; }
  .perk-title { font-weight: 700; font-size: 13px; line-height: 15px; color: var(--ink); }
  .perk-text {
    font-family: "Inter", Arial, sans-serif; font-weight: 300;
    font-size: 11px; line-height: 13.5px; color: var(--body);
  }

  .details-button {
    position: absolute; left: 50%; top: 423px; transform: translateX(-50%);
    width: 89px; height: 30px; background: var(--lime); color: var(--white);
    display: flex; align-items: center; justify-content: center; gap: 4px;
    font-family: "Inter", Arial, sans-serif; font-size: 11.5px; text-decoration: none;
  }

  .apply-button {
    position: absolute; left: 510px; top: 810px; width: 180px; height: 50px;
    background: var(--apply-blue); color: var(--white); border-radius: 6px 6px 0 0;
    display: flex; align-items: center; justify-content: center;
    font-family: "Inter", Arial, sans-serif; font-weight: 300; font-size: 25px; text-decoration: none;
  }
</style>
</head>
<body>
  <div class="top-rule"></div>
  <h2 class="section-title">Card Features</h2>

  <div class="feature feature--benefits">
    <svg class="feature-icon" viewBox="0 0 70 70" aria-hidden="true">
      <circle cx="35" cy="35" r="33.5" fill="none" stroke="var(--ring)" stroke-width="2"/>
      <path d="M44 25c-2-4-6-5-9-5-5 0-9 2-9 7 0 9 18 5 18 15 0 5-4 7-9 7-4 0-8-2-10-6" fill="none" stroke="var(--apply-blue)" stroke-width="4.5" stroke-linecap="round"/>
      <path d="M35 14v42" stroke="var(--apply-blue)" stroke-width="3"/>
    </svg>
    <h3 class="feature-name">Exclusive Benefits</h3>
  </div>

  <div class="feature feature--security">
    <svg class="feature-icon" viewBox="0 0 70 70" aria-hidden="true">
      <circle cx="35" cy="35" r="33.5" fill="none" stroke="var(--ring)" stroke-width="2"/>
      <path d="M27 32v-7a8 8 0 0 1 16 0v7" fill="none" stroke="var(--apply-blue)" stroke-width="2.5"/>
      <rect x="22" y="32" width="26" height="22" rx="4" fill="none" stroke="var(--apply-blue)" stroke-width="2.5"/>
      <circle cx="35" cy="40" r="3" fill="none" stroke="var(--apply-blue)" stroke-width="2"/>
      <path d="M35 43v6" stroke="var(--apply-blue)" stroke-width="2.5" stroke-linecap="round"/>
    </svg>
    <h3 class="feature-name">Security &amp; Safety</h3>
  </div>

  <div class="feature feature--access">
    <svg class="feature-icon" viewBox="0 0 70 70" role="img" aria-label="Map of the continents">
      <circle cx="35" cy="35" r="33.5" fill="none" stroke="var(--ring)" stroke-width="2"/>
      <circle cx="35" cy="35" r="26" fill="#dce7f2"/>
    </svg>
    <h3 class="feature-name">World Wide Access</h3>
  </div>

  <div class="feature-card feature-card--benefits">
    <div class="perk"><p class="perk-title">Osto eosaect empore</p><p class="perk-text">Ipsametus a nempore doluptatius dolorporerum eserias autaerumet facera pra quam hictori aectem sandit, aboriorestem est.</p></div>
    <div class="perk"><p class="perk-title">Omnisinvel endigendant alignisto</p><p class="perk-text">Dollatem nosam, cum sit, tet ditam et magnatisit, coribus.</p></div>
    <div class="perk"><p class="perk-title">Udis ea si cus et as ea que</p><p class="perk-text">Conseni hicillut aut exerspe dipitecerem inveritati re nus modit ad eat reperibea sitio.</p></div>
    <div class="perk"><p class="perk-title">Ut labore dolut occat</p><p class="perk-text">Volorerum que natio et quosae endebis eicae vid mod magnis dent. Agnihicte necus. Xeri dit alit et ulpario ima voluptat harum asimus adis enimoluptat.</p></div>
    <a class="details-button" href="#">More Details <svg width="9" height="12" viewBox="0 0 9 12" aria-hidden="true"><path d="M1 1l4 5-4 5M4 1l4 5-4 5" fill="none" stroke="#fff" stroke-width="1.1"/></svg></a>
  </div>

  <div class="feature-card feature-card--security">
    <div class="perk"><p class="perk-title">Agnihicte necus</p><p class="perk-text">Xeri dit alit et ulpario ima voluptat harum asimus adis enimoluptat.</p></div>
    <div class="perk"><p class="perk-title">Mi, non ped molore</p><p class="perk-text">Erunto voloriti rem ilibus sequias endes dis as doloris eria eate nobis</p></div>
    <div class="perk"><p class="perk-title">Imenisitis arcia voluptatiis</p><p class="perk-text">Minime endi ulparum faces nonse seque comniminus dolum fuga. Exped ento est ex enis ullentiatur sint volum lata ipsam.</p></div>
    <div class="perk"><p class="perk-title">Audae nulpa vellupit eatur</p><p class="perk-text">Nossecea exceria paruntiur magnatatus sunt et ut aut atiuntion rerum ad ut hilloreped et is eost esequas nam latumquati blaccus mos expelenimus, alicat alis dolo bla dis minvel ius etur</p></div>
    <a class="details-button" href="#">More Details <svg width="9" height="12" viewBox="0 0 9 12" aria-hidden="true"><path d="M1 1l4 5-4 5M4 1l4 5-4 5" fill="none" stroke="#fff" stroke-width="1.1"/></svg></a>
  </div>

  <div class="feature-card feature-card--access">
    <div class="perk"><p class="perk-title">Ictataqunti volore lam ea</p><p class="perk-text">Fre explatume commodigent, tem nos magnim ligendam</p></div>
    <div class="perk"><p class="perk-title">Erionsecture nim que rehendis</p><p class="perk-text">Peruntum el mi, estium ni ditemporenis int omnihil</p></div>
    <div class="perk"><p class="perk-title">Ciatio. Erciis dicae vendit</p><p class="perk-text">Ous, qui acero verroressunt quis di dis ad quatius etur.</p></div>
    <div class="perk"><p class="perk-title">Elit lab im quiat autesci</p><p class="perk-text">Psusandit excestecta nonemquatur, coria seniendit, il mint dolupta.</p></div>
    <div class="perk"><p class="perk-title">Auda commolum faccab</p><p class="perk-text">Wes volesci ditaque necumqui cum ipsaectus nonsed que net rehent aliquamus eum ut ditia pa as ne vendaerum rem saerae velisimus et quibus aut maiossuntium utet lis asperum illa ipis alignat.</p></div>
    <a class="details-button" href="#">More Details <svg width="9" height="12" viewBox="0 0 9 12" aria-hidden="true"><path d="M1 1l4 5-4 5M4 1l4 5-4 5" fill="none" stroke="#fff" stroke-width="1.1"/></svg></a>
  </div>

  <a class="apply-button" href="#">Apply now</a>
</body>
</html>
```